Company Capability Brochure

Want to create a mulit paged brochure to hand out to potential clients to show our services and capabilities.

Attached is a rough draft we made using chatgpt which can be use as an example and includes the categories, text, our logo and preferred colour scheme we wish to use.
Would like to make this more look more visually appealing and a more professional layout over more pages.

```html
<!DOCTYPE html>
<html lang="en">
<head>
<meta charset="utf-8">
<title>Vigilant Guard Systems – Capability Brochure</title>
<link href="https://fonts.googleapis.com/css2?family=Audiowide&family=Poppins:wght@400;500;600;700&family=Russo+One&display=swap" rel="stylesheet">
<style>
:root{
  --bg:#e7e4e8;
  --navy:#07145e;
  --navy-mid:#102a92;
  --navy-glow:#1f46c4;
  --blue:#1a7fe0;
  --sky:#2aa4f4;
  --white:#ffffff;
  --ink:#1b1f2e;
  --silver-hi:#f4f5f7;
  --silver:#c3c8d1;
  --silver-lo:#7d8596;
}
*{margin:0;padding:0;box-sizing:border-box}
html,body{width:930px;height:1200px;overflow:hidden;background:var(--bg);font-family:"Poppins",sans-serif;color:var(--ink)}
.page{position:absolute;width:379px;height:490px;overflow:hidden;background:var(--white);box-shadow:0 4px 14px rgba(0,0,0,.18)}
.page--cover{left:68px;top:91px}
.page--back{left:484px;top:91px}
.page--about{left:68px;top:618px}
.page--services{left:484px;top:618px}
.navy-fill{background:radial-gradient(ellipse at 60% 50%,var(--navy-glow) 0%,var(--navy-mid) 42%,var(--navy) 100%)}
.abs{position:absolute}
.wave{position:absolute;left:0;top:0;width:379px;height:490px}

/* brand lockup */
.brand{display:flex;align-items:center;gap:7px;color:var(--sky);font-weight:600;line-height:1}
.brand__dot{width:22px;height:22px;border-radius:50%;background:var(--sky);flex:none}
.brand__name{letter-spacing:2px;font-size:13px}
.brand__sub{display:block;font-size:7px;letter-spacing:3px;margin-top:3px}

/* cover */
.cover__brand{left:104px;top:36px}
.cover__title{left:0;width:379px;top:86px;text-align:center;color:var(--white);font-family:"Russo One",sans-serif;line-height:1}
.cover__title .l1{font-size:27px;display:block}
.cover__title .l2{font-size:48px;display:block;color:var(--sky);margin-top:1px;letter-spacing:1px}
.cover__title .l3{font-size:31px;display:block;margin-top:2px;font-weight:600;font-family:"Poppins",sans-serif;letter-spacing:1px}
.cover__photo{left:98px;top:200px;width:281px;height:226px;border-radius:60px 0 0 90px;
  background:
    radial-gradient(ellipse at 30% 40%,rgba(255,255,255,.9) 0%,rgba(255,255,255,0) 45%),
    linear-gradient(160deg,var(--silver-hi) 0%,var(--silver) 45%,var(--silver-lo) 100%);
  box-shadow:0 10px 30px rgba(3,10,60,.45)}
.tagline{font-family:"Audiowide",sans-serif;line-height:1.17}
.cover__tagline{left:24px;top:349px;color:var(--white);font-size:19px}
.cover__licence{left:24px;top:428px;color:var(--white);font-size:9.5px;font-weight:600;display:flex;align-items:center;gap:4px;letter-spacing:.3px}
.cover__licence b{background:var(--blue);border-radius:6px;padding:1px 8px;font-family:"Audiowide",sans-serif;font-weight:400;font-size:10px}
.cover__url{left:0;width:379px;top:458px;text-align:center;color:var(--white);font-size:9px;letter-spacing:2.3px;font-weight:600}
.cover__url span{color:var(--sky)}

/* back */
.back__brand{left:42px;top:122px;gap:12px}
.back__brand .brand__dot{width:58px;height:58px}
.back__brand .brand__name{font-size:21px;letter-spacing:3px;color:var(--blue)}
.back__brand .brand__sub{font-size:11px;letter-spacing:5.2px;color:var(--blue);margin-top:4px}
.contact{left:24px;top:405px;color:var(--white)}
.contact h3{font-size:11px;font-weight:700;margin-bottom:3px}
.contact li{list-style:none;font-size:7.6px;display:flex;align-items:center;gap:4px;line-height:1.45}
.contact svg{width:7px;height:7px;flex:none}
.back__tagline{left:211px;top:404px;color:var(--sky);font-size:16.5px}

/* about */
.sec-title{font-family:"Audiowide",sans-serif;color:var(--blue);font-size:15px;line-height:1}
.body{font-size:6.1px;line-height:1.2;color:var(--ink)}
.about__photo{left:205px;top:0;width:174px;height:300px;
  background:
    radial-gradient(ellipse at 55% 28%,#ffffff 0%,rgba(255,255,255,0) 40%),
    radial-gradient(ellipse at 45% 72%,#fbfbfc 0%,rgba(255,255,255,0) 38%),
    linear-gradient(90deg,#f6f7f9 0%,#d5d8de 55%,#eceef1 75%,#f7f8fa 100%)}
.about__mission{left:24px;top:24px;width:178px}
.about__vision{left:24px;top:143px;width:178px}
.about__mission .body,.about__vision .body{margin-top:5px}
.culture{left:23px;top:327px;width:335px}
.culture .sec-title{color:var(--white)}
.culture__cols{display:flex;gap:14px;margin-top:13px}
.culture__cols p{color:var(--white);font-size:6px;line-height:1.22}
.culture__cols p:nth-child(1){width:90px}
.culture__cols p:nth-child(2){width:106px}
.culture__cols p:nth-child(3){width:104px}
.foot{left:24px;top:463px;width:335px;display:flex;align-items:center;gap:3px;color:var(--white);font-size:6px;letter-spacing:1.5px;font-weight:600}
.foot span{color:var(--sky)}
.foot i{flex:1;height:1px;background:rgba(255,255,255,.55)}
.foot b{width:7px;height:7px;border-radius:50%;background:var(--blue);font-size:4.5px;color:var(--white);display:flex;align-items:center;justify-content:center;letter-spacing:0}

/* services */
.services__title{left:24px;top:24px}
.svc{position:absolute;left:24px;width:186px}
.svc__head{display:flex;align-items:center}
.svc__tag{background:linear-gradient(90deg,var(--navy-mid),var(--blue));color:var(--white);font-size:8px;font-weight:600;padding:1px 6px;border-radius:0 8px 8px 0;width:94px;line-height:1.3}
.svc__line{flex:1;height:1px;background:var(--blue);position:relative}
.svc__line:after{content:"";position:absolute;right:-1px;top:-1px;width:3px;height:3px;border-radius:50%;background:var(--blue)}
.svc .body{margin-top:5px;font-size:5.3px;line-height:1.22}
.svc-photos{left:235px;top:24px;display:flex;flex-direction:column;gap:5px}
.svc-photo{width:121px;height:61px;border:1.5px solid var(--navy-mid);border-radius:8px}
.clients{left:24px;top:388px;width:335px}
.clients .sec-title{color:var(--white)}
.clients__grid{display:grid;grid-template-columns:repeat(5,61px);gap:6px 7px;margin-top:6px}
.client{height:19px;background:var(--white);border-radius:2px;display:flex;align-items:center;justify-content:center;font-size:6.5px;font-weight:600;color:var(--navy-mid);letter-spacing:.3px}
</style>
</head>
<body>

<!-- Cover -->
<section class="page page--cover navy-fill">
  <div class="abs brand cover__brand"><span class="brand__dot"></span><span><span class="brand__name">VIGILANT</span><span class="brand__sub">Guard Systems</span></span></div>
  <h1 class="abs cover__title"><span class="l1">VIGILANT</span><span class="l2">GUARD</span><span class="l3">SYSTEMS</span></h1>
  <div class="abs cover__photo" role="img" aria-label="Photo of a white bullet CCTV camera on a wall bracket"></div>
  <p class="abs tagline cover__tagline">Be Informed<br>&amp; Make The<br>Right Choice</p>
  <p class="abs cover__licence">MASTER LICENSE <b>40512739</b></p>
  <p class="abs cover__url">www.<span>vigilantguard</span>.com</p>
</section>

<!-- Back cover -->
<section class="page page--back">
  <svg class="wave" viewBox="0 0 379 490" aria-hidden="true">
    <defs><radialGradient id="g1" cx="55%" cy="75%" r="70%"><stop offset="0" stop-color="#1f46c4"/><stop offset=".45" stop-color="#102a92"/><stop offset="1" stop-color="#07145e"/></radialGradient></defs>
    <path d="M0 336 C70 302 140 318 210 340 C290 362 345 320 379 275 L379 490 L0 490Z" fill="url(#g1)"/>
    <path d="M0 328 C70 294 140 310 210 330 C290 352 345 310 379 265" fill="none" stroke="#1a3aa8" stroke-width="4"/>
  </svg>
  <div class="abs brand back__brand"><span class="brand__dot"></span><span><span class="brand__name">VIGILANT</span><span class="brand__sub">Guard Systems</span></span></div>
  <div class="abs contact">
    <h3>CONTACT US</h3>
    <ul>
      <li><svg viewBox="0 0 10 10"><circle cx="5" cy="5" r="5" fill="#2aa4f4"/></svg>1300 555 014</li>
      <li><svg viewBox="0 0 10 10"><circle cx="5" cy="5" r="5" fill="#2aa4f4"/></svg>hello@vigilantguard.com.au</li>
      <li><svg viewBox="0 0 10 10"><circle cx="5" cy="5" r="5" fill="#2aa4f4"/></svg>12/8 Harbour St, Greenvale, NSW 2199</li>
      <li><svg viewBox="0 0 10 10"><circle cx="5" cy="5" r="5" fill="#2aa4f4"/></svg>www.vigilantguard.com.au</li>
    </ul>
  </div>
  <p class="abs tagline back__tagline">Be Informed<br>&amp; Make The<br>Right Choice</p>
</section>

<!-- About -->
<section class="page page--about">
  <div class="abs about__photo" role="img" aria-label="Photo of two white CCTV cameras mounted on a wall"></div>
  <svg class="wave" viewBox="0 0 379 490" aria-hidden="true">
    <defs><radialGradient id="g2" cx="50%" cy="60%" r="70%"><stop offset="0" stop-color="#1f46c4"/><stop offset=".45" stop-color="#102a92"/><stop offset="1" stop-color="#07145e"/></radialGradient></defs>
    <path d="M0 252 C60 225 120 270 200 292 C280 312 345 270 379 208 L379 490 L0 490Z" fill="url(#g2)"/>
    <path d="M0 244 C60 217 120 262 200 284 C280 304 345 262 379 200" fill="none" stroke="#1a3aa8" stroke-width="4"/>
  </svg>
  <div class="abs about__mission">
    <h2 class="sec-title">Mission Statement</h2>
    <p class="body">Our mission is to deliver exceptional service and cutting-edge Electronic and Mechanical Security Solutions that not only meet but consistently exceed our clients' expectations. We are dedicated to ensuring the safety, protection, and peace of mind of those we serve by combining advanced technologies, industry expertise, and a relentless focus on quality, reliability, and customer satisfaction. Through personalized solutions, responsive support, and continuous innovation, we aim to build long-term partnerships and be a trusted name in security.</p>
  </div>
  <div class="abs about__vision">
    <h2 class="sec-title">Vision Statement</h2>
    <p class="body">Our vision is to be the most trusted, innovative, and customer-focused partner in the security industry, renowned for the professional installation, service, and maintenance of Electronic and Mechanical Security Systems. We strive to set the benchmark for excellence by delivering tailored, reliable, and future-ready solutions that protect what matters most to our clients, while building lasting relationships based on integrity, responsiveness, and continuous improvement.</p>
  </div>
  <div class="abs culture">
    <h2 class="sec-title">Culture Statement</h2>
    <div class="culture__cols">
      <p>At the heart of our company is a culture driven by trust, innovation, and service excellence. We are a team of dedicated professionals who take pride in protecting what matters most to our clients through advanced Electronic and Mechanical Security Solutions.</p>
      <p>We cultivate a work environment built on integrity, mutual respect, and accountability, where every team member is empowered to grow, contribute ideas, and take ownership of outcomes. Collaboration, continuous improvement, and a commitment to exceeding expectations define how we operate, both with our clients and each other.</p>
      <p>We embrace change, champion innovation, and remain agile in an evolving industry, always striving to deliver smarter, more reliable, and more secure solutions. Together, we are building not just systems, but lasting partnerships and a safer future.</p>
    </div>
  </div>
  <div class="abs foot">www.<span>vigilantguard</span>.com <i></i><b>1</b></div>
</section>

<!-- Services and clients -->
<section class="page page--services">
  <svg class="wave" viewBox="0 0 379 490" aria-hidden="true">
    <defs><radialGradient id="g3" cx="50%" cy="80%" r="70%"><stop offset="0" stop-color="#1f46c4"/><stop offset=".45" stop-color="#102a92"/><stop offset="1" stop-color="#07145e"/></radialGradient></defs>
    <path d="M0 350 C60 325 130 360 210 372 C290 384 345 352 379 290 L379 490 L0 490Z" fill="url(#g3)"/>
    <path d="M0 342 C60 317 130 352 210 364 C290 376 345 344 379 282" fill="none" stroke="#1a3aa8" stroke-width="4"/>
  </svg>
  <h2 class="abs sec-title services__title">Our Services</h2>
  <div class="svc" style="top:48px"><div class="svc__head"><span class="svc__tag">CCTV Systems</span><span class="svc__line"></span></div>
    <p class="body">We design and install high definition camera systems with remote viewing, smart recording and clear footage, giving you full visibility of your site from any device, day or night.</p></div>
  <div class="svc" style="top:102px"><div class="svc__head"><span class="svc__tag">Access Control</span><span class="svc__line"></span></div>
    <p class="body">Card, fob and keypad entry systems that let you decide who goes where and when, with simple user management and full audit trails for every door.</p></div>
  <div class="svc" style="top:155px"><div class="svc__head"><span class="svc__tag">Intercoms</span><span class="svc__line"></span></div>
    <p class="body">Audio and video intercoms for homes, offices and strata buildings, letting you see and speak with visitors before granting entry, on site or from your phone.</p></div>
  <div class="svc" style="top:209px"><div class="svc__head"><span class="svc__tag">Alarms</span><span class="svc__line"></span></div>
    <p class="body">Monitored intruder alarm systems with motion sensors, sirens and instant alerts, installed to suit your layout and backed by prompt service and regular maintenance checks from our licensed technicians on every site.</p></div>
  <div class="svc" style="top:280px"><div class="svc__head"><span class="svc__tag">Gates</span><span class="svc__line"></span></div>
    <p class="body">Automated sliding and swing gates with secure motors, remote access and safety sensors, built to protect driveways and car parks while keeping entry smooth.</p></div>
  <div class="abs svc-photos">
    <div class="svc-photo" style="background:linear-gradient(120deg,#e6eef4 0%,#9cc0d8 35%,#4f86ad 70%,#2c5878 100%)" role="img" aria-label="Photo of a dome security camera on a pole in front of a glass building"></div>
    <div class="svc-photo" style="background:linear-gradient(100deg,#d8d4cc 0%,#a39d93 40%,#5a5852 75%,#2f3a34 100%)" role="img" aria-label="Photo of a hand using a keypad access reader"></div>
    <div class="svc-photo" style="background:linear-gradient(100deg,#f3f2ef 0%,#dedbd6 45%,#c9c3ba 75%,#9a9184 100%)" role="img" aria-label="Photo of a finger pressing a wall-mounted intercom screen"></div>
    <div class="svc-photo" style="background:linear-gradient(100deg,#3a3632 0%,#c8332b 35%,#ece6d8 65%,#2a66c8 100%)" role="img" aria-label="Photo of alarm sirens and sensors on a wall"></div>
    <div class="svc-photo" style="background:linear-gradient(180deg,#f1f1ef 0%,#9c9892 45%,#4a4744 75%,#bdbab5 100%)" role="img" aria-label="Photo of a modern house with an automated gate"></div>
  </div>
  <div class="abs clients">
    <h2 class="sec-title">Our Clients</h2>
    <div class="clients__grid">
      <span class="client">NORVALE</span>
      <span class="client">Parkmont</span>
      <span class="client">EXWOOD</span>
      <span class="client">APEX</span>
      <span class="client">Brook&amp;Dale</span>
      <span class="client">stratapoint</span>
      <span class="client">PRG STRATA</span>
      <span class="client">Corestrata</span>
      <span class="client">Calder Club</span>
      <span class="client">HARWICK</span>
    </div>
  </div>
  <div class="abs foot">www.<span>vigilantguard</span>.com <i></i><b>2</b></div>
</section>

</body>
</html>
```